Business card design needed

We are a start up Mobile Vet Clinic.
We will be servicing an are that cover the Gladstone Region Shire.
Bookings will be made via the number listed or email address.
Travel will be charged

Target Market(s)

Pet Owners

Industry/Entity Type

Business

Contact Information for Business Card

BRINDELLA MOBILE VET
Tarrowen Pty Ltd
Dana Fosterby BVSc
27 Wexhaven St
Yarrowby KVR 4712

PH: 0743186209 Fax: 0743186514 email: bmvet@quillnet.example

Logo styles of interest
Pictorial/Combination Logo

```html
<!DOCTYPE html>
<html lang="en">
<head>
<meta charset="utf-8">
<title>Brindella Mobile Vet – Business Card</title>
<link rel="stylesheet" href="https://fonts.googleapis.com/css2?family=Catamaran:wght@400;500;600;700&display=swap">
<style>
  :root {
    --ink: #111111;
    --paper: #f5f5f5;
    --paper-soft: #ececec;
  }
  html, body {
    margin: 0;
    padding: 0;
    overflow: hidden;
    background: #ffffff;
  }
  .card {
    position: relative;
    width: 1200px;
    height: 693px;
    overflow: hidden;
    font-family: "Catamaran", sans-serif;
    color: var(--ink);
  }
  .card__backdrop {
    position: absolute;
    inset: 0;
    background: radial-gradient(ellipse at 50% 50%, var(--paper) 0%, var(--paper-soft) 100%);
  }
  .brand {
    position: absolute;
    left: 0;
    top: 0;
    width: 1200px;
    height: 693px;
    margin: 0;
    pointer-events: none;
  }
  .brand__text {
    font-family: "Catamaran", sans-serif;
    font-weight: 600;
    font-size: 97px;
    fill: var(--ink);
  }
  .divider {
    position: absolute;
    left: 637px;
    top: 269px;
    width: 4px;
    height: 162px;
    background: var(--ink);
  }
  .contact {
    position: absolute;
    left: 676px;
    top: 268px;
    margin: 0;
    padding: 0;
    list-style: none;
    font-size: 37px;
    font-weight: 400;
    line-height: 52px;
    white-space: nowrap;
  }
  .contact__label {
    font-weight: 600;
  }
  .address {
    position: absolute;
    right: 48px;
    top: 562px;
    margin: 0;
    font-style: normal;
    font-size: 37px;
    font-weight: 400;
    line-height: 45px;
    text-align: right;
    white-space: nowrap;
  }
</style>
</head>
<body>
  <main class="card">
    <div class="card__backdrop" role="img" aria-label="Light grey geometric hexagon line pattern background"></div>

    <svg class="brand" viewBox="0 0 1200 693" role="heading" aria-level="1" aria-label="Brindella Mobile Vet">
      <text class="brand__text" x="79" y="339" textLength="519" lengthAdjust="spacing">BRINDELLA</text>
      <text class="brand__text" x="79" y="418" textLength="519" lengthAdjust="spacing">MOBILE VET</text>
    </svg>

    <div class="divider"></div>

    <ul class="contact">
      <li><span class="contact__label">Phone:</span> 0743186209</li>
      <li><span class="contact__label">Fax:</span> 0743186514</li>
      <li><span class="contact__label">Email:</span> bmvet@quillnet.example</li>
    </ul>

    <address class="address">
      Tarrowen Pty Ltd Dana Fosterby<br>
      BVSc 27 Wexhaven St Yarrowby KVR 4712
    </address>
  </main>
</body>
</html>
```